Logo and Advertising on Company Vehicle Van

Put Logo along with information on the side and end of a small City Van. Would like it to be colorful and informative. Information should include the following:
"Your Foundation Repair Specialists"
*Foundation Leveling & Repair
*Epoxy Crack Injection
*Carbon Fiber Crack Repair
www.BedrockPilotGroupInc.com

Target Market(s)

Home owners that drive by parked van, or see the van driving on streets and freeways.

Industry/Entity Type

Construction Company

Colors

Designer to choose colors to be used in the design.

Requirements
Must have
• Company Logo (included in download)
• Tag line: Your Foundation Repair Specialists
• Bullet points:
• Foundation Leveling & Repair
• Epoxy Crack Injection
• Carbon Fiber Crack Repair
Nice to have
• Colorful background, maybe picture of a broken House (included in download files) or broken foundation.

```html
<!DOCTYPE html>
<html lang="en">
<head>
<meta charset="utf-8">
<title>Bedrock Pilot Group Inc. – Van Wrap Layout</title>
<link rel="stylesheet" href="https://fonts.googleapis.com/css2?family=Open+Sans:ital,wght@0,400;0,600;0,700;1,700;1,800&display=swap">
<style>
  :root {
    --orange: #ea8424;
    --yellow: #e9c22a;
    --charcoal: #3d3e40;
    --white: #ffffff;
    --backdrop: #e9eaec;
    --ink: #444548;
    --seam: #d4761e;
  }
  html, body { margin: 0; padding: 0; overflow: hidden; }
  body {
    width: 1200px; height: 1179px;
    background: var(--backdrop);
    font-family: "Open Sans", sans-serif;
    position: relative;
  }
  .panel { position: absolute; }
  .panel-bg { position: absolute; left: 0; top: 0; display: block; }
  .side-panel { left: 20px; top: 40px; width: 1160px; height: 470px; }
  .rear-panel { left: 330px; top: 560px; width: 540px; height: 580px; }
  .abs { position: absolute; margin: 0; white-space: nowrap; }

  .brand { display: flex; align-items: center; gap: 22px; }
  .brand-square { background: var(--orange); flex: none; }
  .brand-name { font-weight: 600; color: var(--orange); line-height: 1.05; }
  .side-panel .brand { left: 600px; top: 50px; }
  .side-panel .brand-square { width: 90px; height: 90px; }
  .side-panel .brand-name { font-size: 42px; }
  .side-rule { left: 714px; top: 150px; width: 392px; height: 2px; background: var(--orange); }

  .tagline { font-weight: 800; font-style: italic; text-transform: uppercase; letter-spacing: .2px; }
  .services { list-style: none; padding: 0; }
  .services li::before { content: "•"; }

  .side-panel .tagline {
    left: 712px; top: 196px; font-size: 17px; color: var(--white);
    transform: rotate(-5deg); transform-origin: left bottom;
  }
  .side-panel .services {
    left: 786px; top: 218px; font-size: 15px; color: var(--white); line-height: 1.2;
    transform: rotate(-4deg); transform-origin: left bottom;
  }

  .phone { display: flex; align-items: center; gap: 6px; font-weight: 700; }
  .phone-icon { display: block; flex: none; }
  .side-panel .phone { left: 320px; top: 334px; font-size: 31px; color: var(--orange); }
  .side-panel .web { left: 580px; top: 346px; font-size: 17px; font-weight: 700; font-style: italic; color: var(--white); }

  .rear-panel .brand { left: 45px; top: 40px; gap: 18px; }
  .rear-panel .brand-square { width: 80px; height: 80px; }
  .rear-panel .brand-name { font-size: 36px; }
  .rear-rule { left: 143px; top: 124px; width: 350px; height: 2px; background: var(--orange); }
  .rear-panel .tagline { left: 0; right: 0; top: 148px; text-align: center; font-size: 19.5px; color: var(--orange); }
  .rear-panel .services { left: 140px; top: 178px; font-size: 19px; color: var(--ink); line-height: 1.13; }
  .rear-panel .web { left: 0; right: 0; top: 253px; text-align: center; font-size: 19px; font-weight: 700; font-style: italic; color: var(--white); }
  .rear-panel .phone { left: 68px; top: 408px; font-size: 34px; color: var(--white); }
</style>
</head>
<body>

<section class="panel side-panel" aria-label="Side wrap">
  <svg class="panel-bg" viewBox="0 0 1160 470" width="1160" height="470" aria-hidden="true">
    <rect x="0" y="0" width="1160" height="470" rx="28" fill="var(--white)"/>
    <path d="M0 248 C 250 285, 480 255, 700 195 C 850 160, 1000 150, 1160 142 L1160 470 L0 470 Z" fill="var(--yellow)"/>
    <path d="M0 256 C 250 293, 480 263, 700 203 C 850 168, 1000 158, 1160 150 L1160 470 L0 470 Z" fill="var(--orange)"/>
    <path d="M0 296 C 300 302, 700 292, 1160 270 L1160 470 L0 470 Z" fill="var(--white)"/>
    <path d="M0 304 C 300 310, 700 300, 1160 278 L1160 442 Q1160 470 1132 470 L28 470 Q0 470 0 442 Z" fill="var(--charcoal)"/>
  </svg>
  <div class="abs brand">
    <span class="brand-square"></span>
    <span class="brand-name">Bedrock Pilot<br>Group Inc.</span>
  </div>
  <span class="abs side-rule"></span>
  <p class="abs tagline">Your Foundation Repair Specialists</p>
  <ul class="abs services">
    <li>Foundation Leveling &amp; Repair</li>
    <li>Epoxy Crack Injection</li>
    <li>Carbon Fiber Crack Repair</li>
  </ul>
  <p class="abs phone">
    <svg class="phone-icon" width="18" height="30" viewBox="0 0 14 30" aria-hidden="true"><path d="M8 2 L3 4 Q0 15 5 26 L10 28 L12 22 L8 20 Q6 15 8 10 L12 8 Z" fill="currentColor"/></svg>
    555-014-2290
  </p>
  <p class="abs web">www.BedrockPilotGroupInc.com</p>
</section>

<section class="panel rear-panel" aria-label="Rear wrap">
  <svg class="panel-bg" viewBox="0 0 540 580" width="540" height="580" aria-hidden="true">
    <rect x="0" y="0" width="540" height="580" rx="30" fill="var(--white)"/>
    <path d="M0 244 H540 V550 Q540 580 510 580 H30 Q0 580 0 550 Z" fill="var(--orange)"/>
    <rect x="0" y="244" width="540" height="7" fill="var(--yellow)"/>
    <line x1="270" y1="251" x2="270" y2="580" stroke="var(--seam)" stroke-width="2"/>
  </svg>
  <div class="abs brand">
    <span class="brand-square"></span>
    <span class="brand-name">Bedrock Pilot<br>Group Inc.</span>
  </div>
  <span class="abs rear-rule"></span>
  <p class="abs tagline">Your Foundation Repair Specialists</p>
  <ul class="abs services">
    <li>Foundation Leveling &amp; Repair</li>
    <li>Epoxy Crack Injection</li>
    <li>Carbon Fiber Crack Repair</li>
  </ul>
  <p class="abs web">www.BedrockPilotGroupInc.com</p>
  <p class="abs phone">
    <svg class="phone-icon" width="20" height="34" viewBox="0 0 14 30" aria-hidden="true"><path d="M8 2 L3 4 Q0 15 5 26 L10 28 L12 22 L8 20 Q6 15 8 10 L12 8 Z" fill="currentColor"/></svg>
    555-014-2290
  </p>
</section>

</body>
</html>
```